FRONT BUS CARD:

We were maybe thinking to have the text in a "common seal" which is an oval shape. Or CROWN VAULT underlined, then AUSTRALIA underneath...

Picture to have in the seal, or next to the words if seal not used: Gold Bars (3 of them), or scales of justice..

LOGO and pic and font to be in shiny gold.
We want 1 black background design and 1 white background design.

CROWN VAULT TRADERS

```html
<!DOCTYPE html>
<html lang="en">
<head>
<meta charset="utf-8">
<title>Crown Vault Traders – Business Card Front</title>
<link rel="stylesheet" href="https://fonts.googleapis.com/css2?family=Lilita+One&display=swap">
<style>
  :root {
    --card-white: #ffffff;
    --seal-backdrop: #f3f5f9;
    --frame-gold-light: #fbf3cf;
    --frame-gold: #e7c766;
    --frame-gold-deep: #b98a2c;
    --field-gold-light: #efe3a6;
    --field-gold: #e2cf80;
    --field-gold-deep: #cdb560;
    --edge-brown: #a9692e;
    --name-orange: #e28a12;
  }
  * { margin: 0; padding: 0; box-sizing: border-box; }
  html, body {
    width: 1200px;
    height: 686px;
    overflow: hidden;
    background: var(--card-white);
  }
  .card {
    position: relative;
    width: 1200px;
    height: 686px;
    background: var(--card-white);
  }
  .card__art {
    position: absolute;
    inset: 0;
    width: 1200px;
    height: 686px;
  }
  .seal {
    position: absolute;
    left: 11px;
    top: 11px;
    width: 526px;
    height: 412px;
    display: flex;
    flex-direction: column;
    align-items: center;
    justify-content: center;
    text-align: center;
    font-family: "Lilita One", sans-serif;
    color: var(--name-orange);
    letter-spacing: 1px;
  }
  .seal__name {
    font-size: 42px;
    line-height: 1;
    margin-top: 70px;
  }
  .seal__subline {
    font-size: 30px;
    line-height: 1;
    margin-top: 26px;
  }
</style>
</head>
<body>
  <main class="card">
    <svg class="card__art" viewBox="0 0 1200 686" xmlns="http://www.w3.org/2000/svg">
      <defs>
        <radialGradient id="frame-fill" cx="50%" cy="50%" r="50%">
          <stop offset="0%" stop-color="var(--frame-gold-light)"/>
          <stop offset="72%" stop-color="var(--frame-gold-light)"/>
          <stop offset="86%" stop-color="var(--frame-gold)"/>
          <stop offset="100%" stop-color="var(--frame-gold-deep)"/>
        </radialGradient>
        <linearGradient id="field-fill" x1="0" y1="0" x2="1" y2="1">
          <stop offset="0%" stop-color="var(--field-gold-light)"/>
          <stop offset="55%" stop-color="var(--field-gold)"/>
          <stop offset="100%" stop-color="var(--field-gold-deep)"/>
        </linearGradient>
      </defs>

      <rect class="seal-backdrop" x="6" y="6" width="657" height="440" fill="var(--seal-backdrop)"/>

      <ellipse class="seal-frame" role="img" aria-label="Ornate gold oval frame around the company name"
               cx="274" cy="217" rx="263" ry="206" fill="url(#frame-fill)"/>

      <path class="gold-field" role="img" aria-label="Embossed gold texture panel"
            d="M1076,6 C820,24 650,200 565,360 C475,535 270,655 22,680 L1194,680 L1194,6 Z"
            fill="url(#field-fill)"/>
      <path class="gold-field__edge"
            d="M1076,6 C820,24 650,200 565,360 C475,535 270,655 22,680"
            fill="none" stroke="var(--edge-brown)" stroke-width="4"/>

      <rect class="card-border" x="3" y="3" width="1194" height="680" rx="10" ry="10"
            fill="none" stroke="var(--edge-brown)" stroke-width="5"/>
    </svg>

    <div class="seal">
      <p class="seal__name">CROWN VAULT</p>
      <p class="seal__subline">TRADERS</p>
    </div>
  </main>
</body>
</html>
```